Pellmore Heating & Air

I need a business card made for my company. I would like my new logo for Pellmore Heating and Air on the front and my Garage Door on the back.
Front to say -Heating & Air Conditioning , Mini Splits and Heat Pumps, Hydronic In-Floor Heat. Locally Owned and Operated! Licensed, Boned and Insured. Free Estimates on new equipment. 555-201-4837
KVB Back Card, change phone# to 555-318-6024. Remove Commercial and residential and fully sticked vans lines.

```html
<!DOCTYPE html>
<html lang="en">
<head>
<meta charset="utf-8">
<title>Pellmore Heating &amp; Air – Business Card</title>
<link rel="stylesheet" href="https://fonts.googleapis.com/css2?family=Nunito+Sans:wght@400;600&family=Oswald:wght@500;700&display=swap">
<style>
  :root {
    --red: #e3342a;
    --blue: #1f5289;
    --navy: #17508a;
    --white: #ffffff;
    --backdrop: #e4e4e2;
    --brand-gradient: linear-gradient(90deg, var(--red) 0%, #9a4a5e 50%, var(--blue) 100%);
  }
  * { box-sizing: border-box; margin: 0; padding: 0; }
  html, body { width: 1200px; height: 846px; overflow: hidden; }
  body { background: var(--backdrop); position: relative; font-family: "Nunito Sans", Arial, sans-serif; }

  .card { position: absolute; top: 169px; width: 290px; height: 508px; overflow: hidden; }
  .card--front { left: 280px; background: var(--white); }
  .card--back { left: 630px; background: var(--brand-gradient); color: var(--white); }

  .wordmark { position: absolute; left: 28px; top: 60px; width: 236px; font-family: "Oswald", sans-serif; font-weight: 700; text-align: center; line-height: 1; }
  .wordmark__name { display: block; font-size: 50px; letter-spacing: 1px; }
  .wordmark__tag { display: block; font-size: 27px; letter-spacing: 0.5px; margin-top: 4px; }
  .card--front .wordmark { color: var(--navy); }
  .card--back .wordmark { color: var(--white); }

  .services { position: absolute; left: 28px; list-style: none; }
  .services li { white-space: nowrap; }
  .card--front .services { top: 154px; color: var(--navy); font-size: 16px; line-height: 24.2px; }
  .card--front .services li::before { content: "•"; color: var(--red); margin-right: 2px; }
  .card--back .services { top: 167px; font-size: 15px; line-height: 24px; }
  .card--back .services li::before { content: "•"; font-size: 10px; margin-right: 5px; vertical-align: 2px; }

  .offer-frame { position: absolute; border-radius: 22px; }
  .offer-tab { position: absolute; border-radius: 22px 0 22px 0; text-align: center; }
  .offer-tab__title { font-family: "Oswald", sans-serif; font-weight: 700; display: block; line-height: 1; }
  .offer-tab__sub { display: block; line-height: 1; font-family: "Nunito Sans", sans-serif; }
  .phone { position: absolute; display: flex; align-items: center; gap: 8px; font-family: "Oswald", sans-serif; font-weight: 700; line-height: 1; }

  .card--front .offer-frame { left: 28px; top: 329px; width: 235px; height: 80px; border: 2px solid var(--red); border-right-color: var(--blue); border-bottom-color: #6a4b71; }
  .card--front .offer-tab { left: 38px; top: 295px; width: 215px; height: 60px; background: var(--brand-gradient); color: var(--white); padding-top: 9px; }
  .card--front .offer-tab__title { font-size: 20px; }
  .card--front .offer-tab__sub { font-size: 17px; margin-top: 5px; }
  .card--front .phone { left: 38px; top: 365px; color: var(--navy); font-size: 27px; }

  .site-band { position: absolute; left: 0; bottom: 0; width: 290px; height: 72px; background: var(--brand-gradient); border-radius: 34px 34px 0 0; color: var(--white); text-align: center; font-family: "Oswald", sans-serif; font-weight: 700; line-height: 1.15; padding-top: 14px; }
  .site-band__label { display: block; font-size: 19px; }
  .site-band__url { display: block; font-size: 17px; }

  .card--back .offer-frame { left: 41px; top: 295px; width: 208px; height: 73px; border: 2px solid var(--white); }
  .card--back .offer-tab { left: 58px; top: 267px; width: 175px; height: 53px; background: var(--white); padding-top: 6px; }
  .card--back .offer-tab__title { font-size: 20px; color: #7b4863; }
  .card--back .offer-tab__sub { font-size: 19px; color: var(--red); margin-top: 2px; }
  .card--back .phone { left: 51px; top: 330px; color: var(--white); font-size: 24px; }

  .contact { position: absolute; left: 0; top: 384px; width: 290px; text-align: center; font-family: "Oswald", sans-serif; font-weight: 700; font-size: 17px; line-height: 22px; }
  .save-pill { position: absolute; left: 77px; top: 453px; width: 137px; height: 30px; background: var(--white); border-radius: 0 14px 0 14px; color: var(--red); font-family: "Oswald", sans-serif; font-weight: 700; font-size: 14px; text-align: center; line-height: 30px; letter-spacing: 0.3px; }
</style>
</head>
<body>

<section class="card card--front" aria-label="Front of card">
  <h1 class="wordmark"><span class="wordmark__name">PELLMORE</span><span class="wordmark__tag">HEATING &amp; AIR</span></h1>
  <ul class="services">
    <li>Heating &amp; Air Conditioning</li>
    <li>Mini Splits and Heat Pumps</li>
    <li>Hydronic In-Floor Heat</li>
    <li>Locally Owned and Operated!</li>
    <li>Licensed, Boned and Insured</li>
  </ul>
  <div class="offer-frame"></div>
  <div class="offer-tab">
    <span class="offer-tab__title">— FREE ESTIMATES —</span>
    <span class="offer-tab__sub">ON NEW EQUIPMENT</span>
  </div>
  <div class="phone">
    <svg width="34" height="34" viewBox="0 0 34 34" aria-hidden="true">
      <path d="M6 3c2-1 4 0 5 2l3 6c1 2 0 3-1 4l-2 2c1 3 4 6 7 7l2-2c1-1 2-2 4-1l6 3c2 1 3 3 2 5l-2 3c-2 2-5 2-8 1C13 30 4 21 2 12 1 9 2 6 4 5z" fill="var(--navy)"/>
      <path d="M19 9a6 6 0 0 1 6 6M19 4a11 11 0 0 1 11 11" stroke="var(--red)" stroke-width="2.6" fill="none" stroke-linecap="round"/>
    </svg>
    <span>555-201-4837</span>
  </div>
  <div class="site-band">
    <span class="site-band__label">VISIT OUR WEBSITE</span>
    <span class="site-band__url">www.KVBGarageDoor.com</span>
  </div>
</section>

<section class="card card--back" aria-label="Back of card">
  <h2 class="wordmark"><span class="wordmark__name">PELLMORE</span><span class="wordmark__tag">HEATING &amp; AIR</span></h2>
  <ul class="services">
    <li>Same Day &amp; Emergency Service</li>
    <li>All Major Brands</li>
    <li>Locally Owned and Operated!</li>
  </ul>
  <div class="offer-frame"></div>
  <div class="offer-tab">
    <span class="offer-tab__title"><span style="color:var(--red)">—</span> FREE <span style="color:var(--blue)">—</span></span>
    <span class="offer-tab__sub">SERVICE CALL</span>
  </div>
  <div class="phone">
    <svg width="32" height="32" viewBox="0 0 34 34" aria-hidden="true">
      <path d="M6 3c2-1 4 0 5 2l3 6c1 2 0 3-1 4l-2 2c1 3 4 6 7 7l2-2c1-1 2-2 4-1l6 3c2 1 3 3 2 5l-2 3c-2 2-5 2-8 1C13 30 4 21 2 12 1 9 2 6 4 5z" fill="var(--white)"/>
      <path d="M19 9a6 6 0 0 1 6 6M19 4a11 11 0 0 1 11 11" stroke="var(--white)" stroke-width="2.6" fill="none" stroke-linecap="round"/>
    </svg>
    <span>555-318-6024</span>
  </div>
  <p class="contact">info@kvbgaragedoor.com<br>www.KVBGarageDoor.com</p>
  <div class="save-pill">SAVE THIS CARD!</div>
</section>

</body>
</html>
```